RUV Coffee bag (front and back)

We use black matte bags and have front and back labels. We have a logo but need an attractive and inviting label. The labels will be used for our entire line of coffees. We sell most of our coffee to foodservice establishments (Restaurants, Hotels, Bakeries, Bodegas) and we would like to have these establishments display our bags of coffee to sell retail.
The logo can be used as a whole or using any one of the three components (Logo, image, tag).

Target Market(s)

People who buy the coffee they brew at home from the local shop they get their morning latte.. We are a local coffee company, but we do not sell locally roasted coffee!

Industry/Entity Type

Food

Font styles to use
Other font styles liked:
• something that looks good with our trademarked RUV

Colors

Designer to choose colors to be used in the design.

Requirements
Must have
• Respect Trademarked logo
Nice to have
• It would be nice to have a design that can be used with other mediums (airpot wraps, java jackets, )
Should not have
• Real People

```html
<!DOCTYPE html>
<html lang="en">
<head>
<meta charset="utf-8">
<title>RUV Coffee – Bold Velvet Espresso Label</title>
<link rel="stylesheet" href="https://fonts.googleapis.com/css2?family=Montserrat:ital,wght@0,500;0,600;0,700;0,800;1,500&display=swap">
<style>
  :root {
    --page: #ffffff;
    --label-black: #0c0c0c;
    --gold: #c79e62;
    --gold-light: #dcb97f;
    --gold-dark: #a47d45;
    --tag-white: #ffffff;
    --ink: #111111;
    --brand-red: #d42a22;
  }
  * { box-sizing: border-box; margin: 0; padding: 0; }
  html, body {
    width: 1200px;
    height: 891px;
    overflow: hidden;
    background: var(--page);
  }
  .canvas {
    position: relative;
    width: 1200px;
    height: 891px;
    font-family: "Montserrat", Arial, sans-serif;
  }
  .label {
    position: absolute;
    left: 340px;
    top: 45px;
    width: 520px;
    height: 800px;
    background: var(--label-black);
    border-radius: 5px;
  }
  .label-frame {
    position: absolute;
    inset: 18px;
    border: 2px solid var(--gold);
  }
  .brand-tag {
    position: absolute;
    left: 169px;
    top: 0;
    width: 182px;
    height: 232px;
  }
  .brand-tag svg { position: absolute; inset: 0; }
  .brand-mark {
    position: absolute;
    left: 0;
    right: 0;
    top: 84px;
    display: flex;
    align-items: center;
    justify-content: center;
    gap: 8px;
  }
  .brand-dot {
    width: 16px;
    height: 16px;
    border-radius: 50%;
    background: var(--brand-red);
  }
  .brand-name {
    font-weight: 600;
    font-size: 46px;
    letter-spacing: 2px;
    color: var(--ink);
    line-height: 1;
  }
  .brand-sub {
    position: absolute;
    left: 0;
    right: 0;
    top: 140px;
    text-align: center;
    font-size: 7px;
    font-weight: 600;
    letter-spacing: 0.5px;
    color: var(--ink);
  }
  .product-name {
    position: absolute;
    left: 0;
    right: 0;
    top: 340px;
    text-align: center;
    font-weight: 800;
    font-size: 44px;
    line-height: 1.08;
    color: var(--gold);
    letter-spacing: 0.5px;
  }
  .title-rule {
    position: absolute;
    left: 98px;
    top: 448px;
    width: 324px;
    height: 14px;
  }
  .tagline {
    position: absolute;
    left: 0;
    right: 0;
    top: 477px;
    text-align: center;
    font-style: italic;
    font-weight: 500;
    font-size: 20px;
    color: var(--gold);
  }
  .roast-badge {
    position: absolute;
    left: 147px;
    top: 550px;
    width: 222px;
    height: 55px;
    border-radius: 6px;
    background: linear-gradient(180deg, var(--gold-light), var(--gold) 55%, var(--gold-dark));
    display: flex;
    align-items: center;
    justify-content: center;
    font-weight: 800;
    font-size: 19px;
    color: var(--label-black);
    letter-spacing: 0.3px;
  }
  .net-weight {
    position: absolute;
    left: 0;
    right: 0;
    top: 692px;
    text-align: center;
    font-weight: 700;
    font-size: 17px;
    color: var(--gold);
  }
</style>
</head>
<body>
<main class="canvas">
  <section class="label" aria-label="Front label">
    <div class="label-frame"></div>

    <div class="brand-tag">
      <svg viewBox="0 0 182 232" width="182" height="232" aria-hidden="true">
        <path fill="var(--tag-white)" d="M0 0 H182 V220
          L175 228 L168 220 L161 228 L154 220 L147 228 L140 220 L133 228 L126 220
          L119 228 L112 220 L105 228 L98 220 L91 228 L84 220 L77 228 L70 220
          L63 228 L56 220 L49 228 L42 220 L35 228 L28 220 L21 228 L14 220 L7 228 L0 220 Z"/>
      </svg>
      <div class="brand-mark">
        <span class="brand-dot"></span>
        <span class="brand-name">RUV</span>
      </div>
      <div class="brand-sub">Rivera Union Coffee</div>
    </div>

    <h1 class="product-name">BOLD VELVET<br>ESPRESSO</h1>

    <svg class="title-rule" viewBox="0 0 324 14" aria-hidden="true">
      <path fill="var(--gold)" d="M0 7 Q162 1 324 7 Q162 13 0 7 Z"/>
    </svg>

    <p class="tagline">A rich, classic espresso blend.</p>

    <div class="roast-badge">ESPRESSO ROAST</div>

    <p class="net-weight">2 Lb. Whole Bean Coffee</p>
  </section>
</main>
</body>
</html>
```